Wren Vehicle Polishing (Mobile detail)

I need a business card made up. I'd like it to be different in some form, either raised, embossed, debossed, something cool that stands out. (preferably embossed text somewhere in it). I will be including the Initial png file. Let me know if you need the photoshop of adobe illustrator file to work with.

Information to be included: Text: XXX-XXX-XXXX Phone: XXX-XXX-XXXX Email: wrenpolishcrew@mailbox-demo.net Website: www.socialpage-demo.net/wrenpolishKTR Hours of operation: Mon - Fri 7:00AM to 8:00PM Sat - 10:00AM to 8:00PM

Target Market(s)

Mobile automotive detailing

Industry/Entity Type

Automotive

Contact Information for Business Card

Make it stand out with embossed lettering, I'd also like the background to be glossy black or matte, something that represents a shiny car, black preferred

Requirements
Must have
• A glossy background, or something.
• My logo, pick one of them that best fits your design.
Should not have
• White background,
• something that does not stand out.

```html
<!DOCTYPE html>
<html lang="en">
<head>
<meta charset="utf-8">
<title>Wren Vehicle Polishing – Business Card</title>
<link href="https://fonts.googleapis.com/css2?family=Source+Sans+3:wght@400;600&display=swap" rel="stylesheet">
<style>
  :root {
    --page: #9a9a9a;
    --card-black: #0d0d0d;
    --card-glow: #2a2a2a;
    --accent: #e8501c;
    --silver: #d6d6d6;
    --text-light: #d9d9d9;
    --text-muted: #bdbdbd;
    --divider: #4a4a4a;
  }
  * { box-sizing: border-box; margin: 0; padding: 0; }
  html, body {
    width: 1105px; height: 1200px; overflow: hidden;
    background: var(--page);
    font-family: "Source Sans 3", "Helvetica Neue", Arial, sans-serif;
  }
  .sheet {
    position: relative; width: 1105px; height: 1200px;
    display: flex; flex-direction: column; align-items: center;
    padding-top: 56px; gap: 60px;
  }
  .card {
    position: relative; width: 900px; height: 514px; overflow: hidden;
    background: radial-gradient(ellipse at 50% 35%, var(--card-glow) 0%, var(--card-black) 70%);
  }
  /* front */
  .wave { position: absolute; inset: 0; width: 900px; height: 514px; }
  .brand {
    position: absolute; left: 80px; top: 170px; width: 320px;
    display: flex; align-items: center; gap: 18px;
  }
  .brand-dot {
    flex: none; width: 54px; height: 54px; border-radius: 50%;
    background: var(--accent);
  }
  .brand-name {
    color: var(--silver); font-weight: 600; font-size: 36px; line-height: 1.05;
  }
  .divider {
    position: absolute; left: 430px; top: 105px; width: 1px; height: 233px;
    background: var(--divider);
  }
  .contact { position: absolute; left: 467px; top: 106px; }
  .person-name { color: var(--accent); font-weight: 600; font-size: 30px; line-height: 1.2; }
  .person-role { color: var(--text-muted); font-size: 23px; line-height: 1.2; margin-bottom: 16px; }
  .contact-list { list-style: none; }
  .contact-list li {
    display: flex; align-items: center; gap: 12px;
    color: var(--text-light); font-size: 21px; height: 35px;
  }
  .contact-list svg { flex: none; width: 20px; height: 20px; fill: var(--accent); }
  /* back */
  .back-brand {
    position: absolute; left: 0; right: 0; top: 110px;
    display: flex; flex-direction: column; align-items: center; gap: 18px;
  }
  .back-brand .brand-name { font-size: 40px; text-align: center; }
  .hours { position: absolute; left: 0; right: 0; top: 408px; text-align: center; }
  .hours-title { color: var(--accent); font-weight: 600; font-size: 27px; letter-spacing: 0.5px; }
  .hours-line { color: var(--text-light); font-size: 23px; margin-top: 6px; }
  .hours-line .sep { color: var(--accent); font-weight: 600; }
</style>
</head>
<body>
<main class="sheet">
  <section class="card card-front">
    <svg class="wave" viewBox="0 0 900 514" aria-hidden="true">
      <defs>
        <linearGradient id="silverBand" x1="0" y1="0" x2="1" y2="0">
          <stop offset="0" stop-color="#8c8c8c"/>
          <stop offset="0.4" stop-color="#f2f2f2"/>
          <stop offset="0.75" stop-color="#b8b8b8"/>
          <stop offset="1" stop-color="#ececec"/>
        </linearGradient>
        <linearGradient id="orangeBand" x1="0" y1="0" x2="1" y2="0">
          <stop offset="0" stop-color="#d9400f"/>
          <stop offset="1" stop-color="#f06a22"/>
        </linearGradient>
      </defs>
      <path d="M0,436 C240,505 480,482 640,425 C760,382 850,330 900,298 L900,514 L0,514 Z" fill="url(#silverBand)"/>
      <path d="M0,470 C250,512 500,495 660,450 C780,416 860,385 900,366 L900,514 L0,514 Z" fill="#111"/>
      <path d="M0,482 C250,520 510,500 670,458 C790,426 865,396 900,380 L900,514 L0,514 Z" fill="url(#orangeBand)"/>
    </svg>

    <div class="brand">
      <span class="brand-dot"></span>
      <span class="brand-name">Wren Vehicle Polishing</span>
    </div>

    <div class="divider"></div>

    <div class="contact">
      <p class="person-name">Dale Archer</p>
      <p class="person-role">Detailer</p>
      <ul class="contact-list">
        <li>
          <svg viewBox="0 0 20 20" aria-hidden="true"><path d="M5 1h10a1.5 1.5 0 0 1 1.5 1.5v15A1.5 1.5 0 0 1 15 19H5a1.5 1.5 0 0 1-1.5-1.5v-15A1.5 1.5 0 0 1 5 1zm1 3v10h8V4zm4 11.3a1 1 0 1 0 0 2 1 1 0 0 0 0-2z"/></svg>
          555-210-4836
        </li>
        <li>
          <svg viewBox="0 0 20 20" aria-hidden="true"><path d="M4.5 1.5l3 .5 1.5 4-2 1.5a11 11 0 0 0 5.5 5.5l1.5-2 4 1.5.5 3c0 1.5-1.5 3-3 3C8.5 18.5 1.5 11.5 1.5 4.5c0-1.5 1.5-3 3-3z"/></svg>
          555-307-7192
        </li>
        <li>
          <svg viewBox="0 0 20 20" aria-hidden="true"><path d="M1.5 4h17v1.2L10 11 1.5 5.2zm0 3.2L10 13l8.5-5.8V16h-17z"/></svg>
          wrenpolishcrew@mailbox-demo.net
        </li>
        <li>
          <svg viewBox="0 0 20 20" aria-hidden="true"><rect x="2" y="2" width="16" height="16" rx="2"/></svg>
          /wrenpolishKTR
        </li>
      </ul>
    </div>
  </section>

  <section class="card card-back">
    <div class="back-brand">
      <span class="brand-dot"></span>
      <span class="brand-name">Wren Vehicle Polishing</span>
    </div>
    <div class="hours">
      <p class="hours-title">HOURS OF OPERATION</p>
      <p class="hours-line">Mon - Fri 7:00AM to 8:00PM <span class="sep">|</span> Sat - 10:00AM to 8:00PM</p>
    </div>
  </section>
</main>
</body>
</html>
```